QTM Business Cards

I would like to use deep red (See attached logo), medium grays and white on the card to be used as separators for information using a white font over the red and gray colors. We are a web application design and development firm - specializing in custom software development with a content management solution. Our card needs to reflect innovative and cutting edge company.
I have attached the current card for content purposes - there is a front and back to the card. Open to suggestions on layout.

```html
<!DOCTYPE html>
<html lang="en">
<head>
<meta charset="utf-8">
<title>QTM Tech Group – Business Cards</title>
<link rel="stylesheet" href="https://fonts.googleapis.com/css2?family=Lato:ital,wght@0,400;0,700;0,900;1,400;1,700;1,900&display=swap">
<style>
  :root {
    --stage: #2a2a2c;
    --red: #b81e22;
    --red-light: #c8262a;
    --red-dark: #8e1518;
    --red-deep: #7a1013;
    --white: #ffffff;
    --cream: #efe6cf;
    --ink: #1d1d1d;
    --gray: #4a4a4a;
  }
  * { box-sizing: border-box; margin: 0; padding: 0; }
  html, body { width: 1200px; height: 900px; overflow: hidden; }
  body {
    background: var(--stage);
    font-family: "Lato", Arial, sans-serif;
    position: relative;
  }
  .card {
    position: absolute;
    width: 540px;
    height: 300px;
    background: linear-gradient(120deg, var(--red-light) 0%, var(--red) 55%, #a8191d 100%);
    overflow: hidden;
    box-shadow: 0 14px 30px rgba(0,0,0,.45);
  }
  .card-front { left: 80px; top: 130px; }
  .card-back  { left: 580px; top: 470px; }

  /* Front */
  .front-shadow { position: absolute; left: 0; top: 0; width: 540px; height: 300px; }
  .tagline {
    position: absolute; top: 16px; left: 0; width: 100%;
    text-align: center; color: var(--white);
    font-weight: 900; font-size: 15px; letter-spacing: .3px;
  }
  .info-panel {
    position: absolute; left: 48px; top: 44px; width: 228px; height: 226px;
    background: var(--white);
    padding: 12px 14px 0 20px;
  }
  .fold { position: absolute; right: 0; bottom: 0; width: 56px; height: 34px; }
  .brand {
    color: var(--ink); font-weight: 900; font-size: 34px; line-height: 1;
    letter-spacing: 1px; display: flex; align-items: center; gap: 8px;
  }
  .brand-dot { width: 12px; height: 12px; background: var(--red); border-radius: 50%; }
  .brand-sub {
    color: var(--ink); font-weight: 900; font-size: 11px; letter-spacing: 1.5px;
    margin: 2px 0 10px 40px;
  }
  .contact-list { list-style: none; }
  .contact-list li {
    display: flex; align-items: flex-start; gap: 7px;
    font-size: 9px; line-height: 1.15; color: var(--gray);
    margin-bottom: 6px;
  }
  .contact-list svg { width: 10px; height: 10px; flex: none; fill: var(--ink); }
  .person { position: absolute; left: 330px; top: 112px; color: var(--white); }
  .person-name { font-weight: 900; font-size: 20px; letter-spacing: .5px; }
  .person-title { font-style: italic; font-size: 15px; margin-top: 1px; }

  /* Back */
  .services {
    position: absolute; left: 60px; top: 42px; list-style: none;
    color: var(--white); font-weight: 900; font-style: italic;
    font-size: 14px; line-height: 16.5px; letter-spacing: .3px;
  }
  .services li:nth-child(1)  { padding-left: 54px; }
  .services li:nth-child(2)  { padding-left: 48px; }
  .services li:nth-child(3)  { padding-left: 42px; }
  .services li:nth-child(4)  { padding-left: 36px; }
  .services li:nth-child(5)  { padding-left: 30px; }
  .services li:nth-child(6)  { padding-left: 24px; }
  .services li:nth-child(7)  { padding-left: 18px; }
  .services li:nth-child(8)  { padding-left: 12px; }
  .services li:nth-child(9)  { padding-left: 6px; }
  .services li:nth-child(10) { padding-left: 0; }
  .extrusion { position: absolute; left: 0; top: 0; width: 540px; height: 300px; }
  .logo-panel {
    position: absolute; left: 320px; top: 26px; width: 188px; height: 92px;
    background: var(--white);
    display: flex; flex-direction: column; justify-content: center; align-items: center;
  }
  .logo-panel .brand { font-size: 34px; }
  .logo-panel .brand-sub { margin: 2px 0 0 30px; }
  .logo-panel .fold { width: 30px; height: 16px; }
  .social { position: absolute; right: 72px; top: 210px; display: flex; gap: 12px; }
  .social span { width: 22px; height: 22px; background: #3d73b5; border-radius: 3px; }
  .social span.wide { width: 50px; background: var(--white); }
  .follow {
    position: absolute; right: 80px; top: 244px; color: var(--white);
    font-style: italic; font-size: 13px;
  }
  .follow b { font-weight: 900; }
</style>
</head>
<body>

<section class="card card-front" aria-label="Business card front">
  <svg class="front-shadow" viewBox="0 0 540 300" aria-hidden="true">
    <polygon points="48,270 0,300 0,170 48,44" fill="var(--red-dark)" opacity=".55"/>
    <polygon points="48,270 276,270 226,300 0,300" fill="var(--red-dark)" opacity=".75"/>
  </svg>
  <p class="tagline">WOMAN OWNED SMALL BUSINESS</p>
  <div class="info-panel">
    <div class="brand"><span class="brand-dot"></span>QTM</div>
    <div class="brand-sub">TECH GROUP</div>
    <ul class="contact-list">
      <li><svg viewBox="0 0 10 10"><path d="M5 0a3.4 3.4 0 0 0-3.4 3.4C1.6 6 5 10 5 10s3.4-4 3.4-6.6A3.4 3.4 0 0 0 5 0zm0 4.8a1.4 1.4 0 1 1 0-2.8 1.4 1.4 0 0 1 0 2.8z"/></svg>2870 Harbor Point Dr Suite 310<br>Linden, MD 20915</li>
      <li><svg viewBox="0 0 10 10"><path d="M2 0l2 2.4-1 1.2a6 6 0 0 0 3.4 3.4l1.2-1L10 8l-1.4 2C4 10 0 6 0 1.4z"/></svg>555 - 301 - 4420</li>
      <li><svg viewBox="0 0 10 10"><path d="M2 0h5v3H2zM0 3.6h10V9H0zm2 1.4v1h2V5zm4 0v1h2V5zm-4 2v1h6V7z"/></svg>555 - 301 - 4421</li>
      <li><svg viewBox="0 0 10 10"><path d="M2.4 0h5.2c.5 0 .8.3.8.8v8.4c0 .5-.3.8-.8.8H2.4c-.5 0-.8-.3-.8-.8V.8c0-.5.3-.8.8-.8zm.6 1.2v6.4h4V1.2z"/></svg>555 - 742 - 1188</li>
      <li><svg viewBox="0 0 10 10"><path d="M0 1.5h10v7H0zm1 1v.4l4 2.6 4-2.6v-.4z"/></svg>dana@qtmtechgroup.com</li>
      <li><svg viewBox="0 0 10 10"><path d="M5 0a5 5 0 1 0 0 10A5 5 0 0 0 5 0zm3.7 4.4H7.2A7 7 0 0 0 6.5 1.4a4 4 0 0 1 2.2 3zM5 1.2c.5.7.9 1.8 1 3.2H4c.1-1.4.5-2.5 1-3.2zM3.5 1.4a7 7 0 0 0-.7 3H1.3a4 4 0 0 1 2.2-3zM1.3 5.6h1.5c.1 1.2.3 2.2.7 3a4 4 0 0 1-2.2-3zM5 8.8c-.5-.7-.9-1.8-1-3.2h2c-.1 1.4-.5 2.5-1 3.2zm1.5-.2c.4-.8.6-1.8.7-3h1.5a4 4 0 0 1-2.2 3z"/></svg>www.qtmtech.com</li>
    </ul>
    <svg class="fold" viewBox="0 0 56 34" aria-hidden="true">
      <polygon points="56,0 56,34 0,34" fill="var(--red)"/>
      <polygon points="56,0 0,34 14,6" fill="var(--cream)"/>
    </svg>
  </div>
  <div class="person">
    <p class="person-name">DANA WHITCOMB</p>
    <p class="person-title">President</p>
  </div>
</section>

<section class="card card-back" aria-label="Business card back">
  <svg class="extrusion" viewBox="0 0 540 300" aria-hidden="true">
    <polygon points="320,26 300,58 300,148 488,148 508,118 320,118" fill="var(--red-deep)"/>
  </svg>
  <ul class="services">
    <li>PROJECT MGMT/STRATEGY</li>
    <li>WEB APP DEVELOPMENT</li>
    <li>MOBILE APP</li>
    <li>DESIGN</li>
    <li>SECTION 508</li>
    <li>TRAINING</li>
    <li>STAFFING</li>
    <li>SOCIAL MEDIA</li>
    <li>ADVERTISTING</li>
    <li>MARKETING</li>
  </ul>
  <div class="logo-panel">
    <div class="brand"><span class="brand-dot"></span>QTM</div>
    <div class="brand-sub">TECH GROUP</div>
    <svg class="fold" viewBox="0 0 30 16" aria-hidden="true" style="position:absolute;right:0;bottom:0">
      <polygon points="30,0 30,16 0,16" fill="var(--red)"/>
      <polygon points="30,0 0,16 8,3" fill="var(--cream)"/>
    </svg>
  </div>
  <div class="social" aria-label="Social media links">
    <span></span><span></span><span></span><span class="wide"></span>
  </div>
  <p class="follow">Follow us: <b>@QTMTECHGROUP</b></p>
</section>

</body>
</html>
```